Honey Jar Label Design

I am looking for a fun label design for a 1 lb honey jar.
The company is Rosalind Oakhurst Botanicals, which sells cut flowers and is expanding into honey and eventually other honey products. I've included the design work for the business, and I'd like the honey products to coordinate with them but not necessarily match directly.
Label requirements:
Raw Honey
Rosalind Oakhurst Botanicals
27308 Pebble Hollow Rd
Fernvale, NE 66841
NET WT. 16 OZ. (weight info must be in the lower third of the front label and easy to read)
Look and feel
Each slider illustrates characteristics of the customer's brand and the style your logo design should communicate.

```html
<!DOCTYPE html>
<html lang="en">
<head>
<meta charset="utf-8">
<title>Rosalind Oakhurst Botanicals – Raw Honey Label</title>
<link rel="stylesheet" href="https://fonts.googleapis.com/css2?family=Oswald:wght@600&family=Tinos:wght@400;700&display=swap">
<style>
  :root {
    --bg-top: #2a4650;
    --bg-mid: #6f7f86;
    --bg-bottom: #e4e6e8;
    --blush: #eddcda;
    --deep-teal: #1d3c45;
    --cream: #f5ecea;
  }
  * { box-sizing: border-box; margin: 0; padding: 0; }
  html, body { width: 939px; height: 1200px; overflow: hidden; }
  body {
    background: linear-gradient(180deg, var(--bg-top) 0%, var(--bg-mid) 45%, var(--bg-bottom) 100%);
    position: relative;
    font-family: "Tinos", "Times New Roman", serif;
  }
  .front-label {
    position: absolute;
    left: 212px; top: 425px;
    width: 318px; height: 565px;
    background: var(--blush);
    border-radius: 159px 159px 46px 46px / 80px 80px 40px 40px;
    overflow: hidden;
  }
  .brand-seal {
    position: absolute;
    left: 50%; top: 12px;
    transform: translateX(-50%);
    width: 146px; height: 146px;
    border: 2px solid var(--deep-teal);
    border-radius: 50%;
    display: flex; align-items: center; justify-content: center;
    text-align: center;
    color: var(--deep-teal);
    font-size: 15px;
    line-height: 1.25;
    letter-spacing: 0.06em;
    text-transform: uppercase;
    padding: 0 16px;
  }
  .bee-mark {
    position: absolute;
    left: 55px; top: 198px;
    width: 96px; height: 53px;
    background: linear-gradient(180deg, #2a4a53, var(--deep-teal));
  }
  .product-word {
    position: absolute;
    font-family: "Oswald", "Arial Narrow", sans-serif;
    font-weight: 600;
    color: var(--deep-teal);
    line-height: 1;
    white-space: nowrap;
    transform-origin: left top;
  }
  .word-raw {
    left: 153px; top: 185px;
    font-size: 71px;
    transform: scaleX(0.84);
  }
  .word-honey {
    left: 55px; top: 238px;
    font-size: 96px;
    transform: scaleX(0.82);
  }
  .info-band {
    position: absolute;
    left: 0; right: 0; bottom: 0;
    height: 222px;
    background: var(--deep-teal);
    color: var(--cream);
    text-align: center;
    padding-top: 22px;
  }
  .address { font-size: 23px; line-height: 28px; }
  .net-weight {
    margin-top: 18px;
    font-size: 25px;
    font-weight: 700;
    letter-spacing: 0.02em;
  }
  .round-sticker {
    position: absolute;
    left: 578px; top: 259px;
    width: 176px; height: 176px;
    border-radius: 50%;
    background: var(--blush);
    border: 6px solid var(--deep-teal);
    box-shadow: inset 0 0 0 8px var(--blush), inset 0 0 0 9px var(--deep-teal);
    display: flex; align-items: center; justify-content: center;
    text-align: center;
    color: var(--deep-teal);
    font-size: 17px;
    line-height: 1.2;
    letter-spacing: 0.06em;
    text-transform: uppercase;
    padding: 0 22px;
  }
</style>
</head>
<body>
  <section class="front-label">
    <div class="brand-seal">Rosalind Oakhurst Botanicals</div>
    <div class="bee-mark" role="img" aria-label="Bee illustration on a dark panel"></div>
    <div class="product-word word-raw">RAW</div>
    <div class="product-word word-honey">HONEY</div>
    <div class="info-band">
      <p class="address">Rosalind Oakhurst Botanicals<br>27308 Pebble Hollow Rd<br>Fernvale, NE 66841</p>
      <p class="net-weight">NET WT. 16 OZ.</p>
    </div>
  </section>
  <div class="round-sticker">Rosalind Oakhurst Botanicals</div>
</body>
</html>
```